Post Lockdown Ortho Special

We are running a special for (Ortho) Braces/Clear Aligner (Quorventa), till July 31st 2020. Up to $2,000 off with free Consultation and Xrays.

We need a ad to run in different formats.

Maybe something with: what better time to get braces when you have to wear a mask all the time.

Trying to rebuild our business and get people in for free consultations.

```html
<!DOCTYPE html>
<html lang="en">
<head>
<meta charset="utf-8">
<title>Pinecrest Family Dentistry – Post Lockdown Ortho Special</title>
<link rel="stylesheet" href="https://fonts.googleapis.com/css2?family=Montserrat:wght@300;400;600;700&family=Roboto:wght@500;700&display=swap">
<style>
  :root{
    --purple:#6a4a9c;
    --lilac:#dccbe3;
    --white:#ffffff;
    --page:#e8e8e8;
    --skin-1:#f6e3d8;
    --skin-2:#e9c3ae;
    --hair:#7a5646;
  }
  *{box-sizing:border-box;margin:0;padding:0}
  html,body{width:1200px;height:1200px;overflow:hidden;background:var(--page)}
  body{position:relative;font-family:"Montserrat",Arial,sans-serif;color:var(--white)}

  .banner{position:absolute;background:var(--white);overflow:hidden;box-shadow:0 2px 4px rgba(0,0,0,.18)}
  .banner__shape{position:absolute;inset:0;width:100%;height:100%}
  .banner__shape .lilac{fill:var(--lilac)}
  .banner__shape .purple{fill:var(--purple)}

  .photo{position:absolute;border-radius:48% 48% 0 0;
    background:radial-gradient(ellipse at 50% 35%,var(--skin-1) 0%,var(--skin-2) 45%,rgba(233,195,174,.25) 75%,rgba(255,255,255,0) 100%)}

  .brand{position:absolute;display:flex;align-items:center;color:var(--purple);font-weight:600}
  .brand__dot{border-radius:50%;background:var(--purple);flex:none}
  .brand__text{display:flex;flex-direction:column;line-height:1.15;letter-spacing:.06em}
  .brand__name{text-transform:uppercase}
  .brand__sub{text-transform:uppercase;font-size:.34em;letter-spacing:.28em}

  .offer{position:absolute;border:solid var(--white);display:flex;flex-direction:column;align-items:center;justify-content:center;text-align:center;font-family:"Roboto",Arial,sans-serif}
  .offer__upto{display:flex;align-items:center;gap:.9em;font-weight:700;letter-spacing:.14em}
  .offer__upto::before,.offer__upto::after{content:"";display:block;width:3.6em;height:1px;background:var(--white)}
  .offer__amount{display:flex;align-items:center;font-weight:500;line-height:1;letter-spacing:-.03em}
  .offer__dollar{font-size:.42em;align-self:flex-start;margin-right:.08em;font-weight:400}
  .offer__off{writing-mode:vertical-rl;transform:rotate(180deg);font-size:.28em;font-weight:700;letter-spacing:.05em;margin-left:.12em}
  .offer__free{font-weight:500;line-height:1.2}
  .offer__date{font-family:"Montserrat",Arial,sans-serif;font-weight:400}

  .tagline{position:absolute;text-align:center;font-weight:300;line-height:1.42}
  .tagline--bold{font-weight:600}
  .web{position:absolute;font-weight:700;font-family:"Roboto",Arial,sans-serif}

  /* leaderboard */
  .banner--leader{left:438px;top:115px;width:694px;height:88px}
  .banner--leader .offer{border:none;left:26px;top:8px;align-items:flex-start;text-align:left}
  .banner--leader .offer__upto{font-size:12px}
  .banner--leader .offer__upto::before,.banner--leader .offer__upto::after{display:none}
  .banner--leader .offer__amount{font-size:34px}
  .banner--leader .offer__free{font-size:9.5px;font-weight:700}
  .banner--leader .offer__date{font-size:10px;margin-left:22px}
  .banner--leader .tagline{left:190px;width:220px;top:13px;font-size:15.5px;line-height:1.23}
  .banner--leader .brand{left:510px;top:14px;font-size:17px}
  .banner--leader .brand__dot{width:46px;height:46px;margin-right:8px}
  .banner--leader .web{left:551px;top:70px;font-size:8px;color:var(--purple)}

  /* square */
  .banner--square{left:95px;top:254px;width:420px;height:351px}
  .banner--square .offer{left:32px;top:61px;width:138px;height:115px;border-width:2px}
  .banner--square .offer__upto{font-size:11px}
  .banner--square .offer__upto::before,.banner--square .offer__upto::after{width:30px}
  .banner--square .offer__amount{font-size:37px}
  .banner--square .offer__free{font-size:11px}
  .banner--square .offer__date{font-size:6px;margin-top:3px}
  .banner--square .tagline{left:0;width:200px;top:196px;font-size:14.5px}
  .banner--square .web{left:47px;top:331px;font-size:7.5px}
  .banner--square .brand{left:238px;top:14px;font-size:17px}
  .banner--square .brand__dot{width:46px;height:46px;margin-right:10px}

  /* skyscraper narrow */
  .banner--sky{left:622px;top:251px;width:179px;height:354px}
  .banner--sky .tagline{left:0;width:179px;top:14px;font-size:9.6px}
  .banner--sky .offer{left:56px;top:66px;width:78px;height:65px;border-width:1.5px}
  .banner--sky .offer__upto{font-size:6px}
  .banner--sky .offer__upto::before,.banner--sky .offer__upto::after{width:16px}
  .banner--sky .offer__amount{font-size:21px}
  .banner--sky .offer__free{font-size:6px;font-weight:700}
  .banner--sky .offer__date{font-size:3.5px;margin-top:2px}
  .banner--sky .brand{left:12px;top:158px;font-size:7.5px}
  .banner--sky .brand__dot{width:20px;height:20px;margin-right:4px}
  .banner--sky .web{left:51px;top:341px;font-size:7.5px;color:var(--purple)}

  /* skyscraper wide */
  .banner--tall{left:865px;top:250px;width:238px;height:358px}
  .banner--tall .tagline{left:0;width:238px;top:16px;font-size:12px;line-height:1.85}
  .banner--tall .offer{left:14px;top:182px;width:76px;height:64px;border-color:var(--purple);border-width:1.5px;color:var(--purple)}
  .banner--tall .offer__upto{font-size:6px}
  .banner--tall .offer__upto::before,.banner--tall .offer__upto::after{width:16px;background:var(--purple)}
  .banner--tall .offer__amount{font-size:20px}
  .banner--tall .offer__free{font-size:6px;font-weight:700}
  .banner--tall .offer__date{font-size:3.5px;margin-top:2px}
  .banner--tall .brand{left:11px;top:127px;font-size:10.5px}
  .banner--tall .brand__dot{width:26px;height:26px;margin-right:6px}
  .banner--tall .web{left:11px;top:287px;font-size:7.5px;color:var(--purple)}

  /* large landscape */
  .banner--large{left:95px;top:636px;width:1014px;height:432px}
  .banner--large .offer{left:130px;top:32px;width:211px;height:174px;border-width:3px}
  .banner--large .offer__upto{font-size:16px}
  .banner--large .offer__upto::before,.banner--large .offer__upto::after{width:48px}
  .banner--large .offer__amount{font-size:60px;margin:2px 0}
  .banner--large .offer__free{font-size:17.5px}
  .banner--large .offer__date{font-size:10px;margin-top:3px}
  .banner--large .tagline{left:20px;width:424px;top:227px;font-size:27px;line-height:1.45}
  .banner--large .web{left:123px;top:390px;font-size:18px;letter-spacing:.02em}
  .banner--large .brand{left:636px;top:20px;font-size:29px}
  .banner--large .brand__dot{width:88px;height:88px;margin-right:14px}
</style>
</head>
<body>

  <!-- Leaderboard -->
  <section class="banner banner--leader">
    <svg class="banner__shape" viewBox="0 0 694 88" preserveAspectRatio="none" aria-hidden="true">
      <path class="lilac" d="M0 0H494C510 30 510 60 482 88H0Z"/>
      <path class="purple" d="M0 0H484C498 30 496 60 470 88H0Z"/>
    </svg>
    <div class="offer">
      <span class="offer__upto">UP TO</span>
      <span class="offer__amount"><span class="offer__dollar">$</span>2,000<span class="offer__off">OFF</span></span>
      <span class="offer__free">FREE Consultation &amp; Xrays</span>
      <span class="offer__date">’til July 31<sup>st</sup> 2020</span>
    </div>
    <p class="tagline">what better time to get braces when you have to wear a mask all the time</p>
    <div class="brand"><span class="brand__dot"></span><span class="brand__text"><span class="brand__name">Pinecrest</span><span class="brand__sub">Family Dentistry</span></span></div>
    <span class="web">www.websitename.com</span>
  </section>

  <!-- Square -->
  <section class="banner banner--square">
    <svg class="banner__shape" viewBox="0 0 420 351" preserveAspectRatio="none" aria-hidden="true">
      <path class="lilac" d="M0 0H225C252 110 250 240 200 351H0Z"/>
      <path class="purple" d="M0 0H175C225 100 235 240 157 351H0Z"/>
    </svg>
    <div class="photo" role="img" aria-label="Photo of a smiling young woman wearing braces" style="left:240px;top:92px;width:180px;height:259px"></div>
    <div class="offer">
      <span class="offer__upto">UP TO</span>
      <span class="offer__amount"><span class="offer__dollar">$</span>2,000<span class="offer__off">OFF</span></span>
      <span class="offer__free">FREE Consultation<br>and Xrays</span>
      <span class="offer__date">’till July 31<sup>st</sup> 2020</span>
    </div>
    <p class="tagline">what better time<br>to get braces<br>when you have to<br>wear a mask all the time</p>
    <span class="web">www.websitename.com</span>
    <div class="brand"><span class="brand__dot"></span><span class="brand__text"><span class="brand__name">Pinecrest</span><span class="brand__sub">Family Dentistry</span><span class="brand__sub">Dr Helena Marsh</span></span></div>
  </section>

  <!-- Narrow skyscraper -->
  <section class="banner banner--sky">
    <svg class="banner__shape" viewBox="0 0 179 354" preserveAspectRatio="none" aria-hidden="true">
      <path class="lilac" d="M0 0H179V152C130 132 60 130 0 148Z"/>
      <path class="purple" d="M0 0H179V138C120 118 50 124 0 134Z"/>
    </svg>
    <div class="photo" role="img" aria-label="Photo of a smiling young woman wearing braces" style="left:60px;top:166px;width:119px;height:188px"></div>
    <p class="tagline">what better time to get braces<br>when you have to wear a mask<br>all the time</p>
    <div class="offer">
      <span class="offer__upto">UP TO</span>
      <span class="offer__amount"><span class="offer__dollar">$</span>2,000<span class="offer__off">OFF</span></span>
      <span class="offer__free">FREE Consultation<br>and Xrays</span>
      <span class="offer__date">’til July 31st 2020</span>
    </div>
    <div class="brand"><span class="brand__dot"></span><span class="brand__text"><span class="brand__name">Pinecrest</span></span></div>
    <span class="web">www.websitename.com</span>
  </section>

  <!-- Wide skyscraper -->
  <section class="banner banner--tall">
    <svg class="banner__shape" viewBox="0 0 238 358" preserveAspectRatio="none" aria-hidden="true">
      <path class="lilac" d="M0 0H238V122C170 100 90 104 40 112Z"/>
      <path class="purple" d="M0 0H238V100C180 125 70 126 0 96Z"/>
    </svg>
    <div class="photo" role="img" aria-label="Photo of a smiling young woman wearing braces" style="left:112px;top:148px;width:126px;height:210px"></div>
    <p class="tagline tagline--bold">what better time to get braces<br>when you have to wear a mask<br>all the time</p>
    <div class="brand"><span class="brand__dot"></span><span class="brand__text"><span class="brand__name">Pinecrest</span><span class="brand__sub">Dr Helena Marsh</span></span></div>
    <div class="offer">
      <span class="offer__upto">UP TO</span>
      <span class="offer__amount"><span class="offer__dollar">$</span>2,000<span class="offer__off">OFF</span></span>
      <span class="offer__free">FREE Consultation<br>and Xrays</span>
      <span class="offer__date">’til July 31st 2020</span>
    </div>
    <span class="web">www.websitename.com</span>
  </section>

  <!-- Large landscape -->
  <section class="banner banner--large">
    <svg class="banner__shape" viewBox="0 0 1014 432" preserveAspectRatio="none" aria-hidden="true">
      <path class="lilac" d="M0 0H590C620 120 612 300 560 432H0Z"/>
      <path class="purple" d="M0 0H531C600 130 605 300 535 432H0Z"/>
    </svg>
    <div class="photo" role="img" aria-label="Photo of a smiling young woman wearing braces" style="left:630px;top:126px;width:384px;height:306px"></div>
    <div class="offer">
      <span class="offer__upto">UP TO</span>
      <span class="offer__amount"><span class="offer__dollar">$</span>2,000<span class="offer__off">OFF</span></span>
      <span class="offer__free">FREE Consultation<br>and Xrays</span>
      <span class="offer__date">’till July 31<sup>st</sup> 2020</span>
    </div>
    <p class="tagline">what better time to get braces<br>when you have to wear a mask<br>all the time</p>
    <span class="web">www.websitename.com</span>
    <div class="brand"><span class="brand__dot"></span><span class="brand__text"><span class="brand__name">Pinecrest</span><span class="brand__sub">Family Dentistry</span><span class="brand__sub">Dr Helena Marsh</span></span></div>
  </section>

</body>
</html>
```